Business Card for a mobile physiotherapy company

I need a layout for a business card for a mobile physiotherapy company.
Slogan is "Mobile Physiotherapy - Your Road To Recovery"
Phone number is 867-402-5913
Email VantrePhysio@mailbright.ca (subject to change with website)
Website www.VantrePhysio.ca
My name and credentials: Kent Vantre Kent Vantre, BSc(kin), MPT, CAFCI, IMS
Information maybe included: Direct Billing, Services including Physiotherapy, IMS, acupuncture
Maybe include facebook and instagram logos
One side with the logo clean and sharp
Other side with details, try not to look too busy, keep everything concise

```html
<!DOCTYPE html>
<html lang="en">
<head>
<meta charset="utf-8">
<title>Vantre Therapy – Business Card</title>
<link href="https://fonts.googleapis.com/css2?family=Questrial&family=Mulish:wght@700&display=swap" rel="stylesheet">
<style>
  :root {
    --page: #dedede;
    --card-light: #e6e6e6;
    --navy: #27406a;
    --grey-text: #6b6b6b;
    --rule: #7a7a7a;
    --white: #f4f4f4;
  }
  * { box-sizing: border-box; margin: 0; padding: 0; }
  html, body {
    width: 1200px; height: 1200px; overflow: hidden;
    background: var(--page);
    font-family: "Questrial", sans-serif;
  }
  .card {
    position: absolute; left: 227px; width: 746px; height: 425px;
  }
  .card-front { top: 135px; background: var(--card-light); }
  .card-back { top: 640px; background: var(--navy); }

  .brand-mark {
    position: absolute; text-align: center;
    font-family: "Questrial", sans-serif; font-weight: 400;
  }
  .card-front .brand-mark {
    right: 36px; top: 140px; width: 200px; color: var(--navy);
  }
  .brand-name { display: block; font-size: 38px; letter-spacing: 5px; line-height: 1; }
  .brand-sub { display: block; font-size: 19px; letter-spacing: 10px; margin-top: 12px; padding-left: 10px; }

  .holder { position: absolute; left: 33px; top: 238px; }
  .holder-name {
    font-family: "Mulish", sans-serif; font-weight: 700;
    font-size: 23px; color: var(--navy); letter-spacing: 0.2px;
  }
  .holder-creds { font-size: 16px; color: var(--grey-text); margin-top: 6px; }

  .divider { position: absolute; left: 0; right: 0; top: 304px; height: 1px; background: var(--rule); }
  .divider-accent { position: absolute; left: 36px; width: 240px; top: 303px; height: 2px; background: var(--navy); }

  .contacts { position: absolute; left: 33px; top: 322px; list-style: none; }
  .contacts li {
    display: flex; align-items: center; gap: 9px;
    height: 24px; font-size: 17px; color: var(--grey-text);
  }
  .contacts svg { width: 19px; height: 19px; flex: none; }

  .services {
    position: absolute; right: 36px; top: 322px; list-style: none; text-align: right;
  }
  .services li {
    height: 24px; line-height: 24px; font-size: 17px; color: var(--grey-text);
  }
  .services li::after {
    content: ""; display: inline-block; width: 7px; height: 7px; border-radius: 50%;
    background: var(--navy); margin-left: 8px; vertical-align: middle;
  }

  .card-back .brand-mark {
    left: 0; right: 0; top: 170px; color: var(--white);
  }
  .card-back .brand-name { font-size: 46px; letter-spacing: 7px; }
  .card-back .brand-sub { font-size: 21px; letter-spacing: 12px; }
  .slogan {
    position: absolute; left: 0; right: 0; top: 300px; text-align: center;
    font-size: 18px; color: var(--white); letter-spacing: 0.3px;
  }
  .social { position: absolute; top: 361px; left: 0; right: 0; display: flex; justify-content: center; gap: 7px; }
  .social-dot { width: 28px; height: 28px; border-radius: 50%; background: var(--white); }
</style>
</head>
<body>
  <section class="card card-front">
    <div class="brand-mark">
      <span class="brand-name">VANTRE</span>
      <span class="brand-sub">THERAPY</span>
    </div>

    <div class="holder">
      <h1 class="holder-name">Kent Vantre Kent Vantre</h1>
      <p class="holder-creds">BSc(kin), MPT, CAFCI, IMS</p>
    </div>

    <div class="divider"></div>
    <div class="divider-accent"></div>

    <ul class="contacts">
      <li>
        <svg viewBox="0 0 20 20" aria-hidden="true"><circle cx="10" cy="10" r="10" fill="#27406a"/><path d="M6.5 5.2l2 2-1 1.3c.7 1.5 1.9 2.7 3.4 3.4l1.3-1 2 2-1.2 1.4c-3.5-.4-7.4-4.3-7.8-7.8z" fill="#e6e6e6"/></svg>
        867-402-5913
      </li>
      <li>
        <svg viewBox="0 0 20 20" aria-hidden="true"><circle cx="10" cy="10" r="10" fill="#27406a"/><rect x="5" y="6.5" width="10" height="7" fill="none" stroke="#e6e6e6" stroke-width="1.1"/><path d="M5 6.5l5 4 5-4" fill="none" stroke="#e6e6e6" stroke-width="1.1"/></svg>
        VantrePhysio@mailbright.ca
      </li>
      <li>
        <svg viewBox="0 0 20 20" aria-hidden="true"><circle cx="10" cy="10" r="10" fill="#27406a"/><g fill="none" stroke="#e6e6e6" stroke-width="1"><circle cx="10" cy="10" r="5.5"/><ellipse cx="10" cy="10" rx="2.4" ry="5.5"/><path d="M4.5 10h11M5.5 7.2h9M5.5 12.8h9"/></g></svg>
        www.VantrePhysio.ca
      </li>
    </ul>

    <ul class="services">
      <li>Direct Billing</li>
      <li>Services including Physiotherapy</li>
      <li>IMS, acupuncture</li>
    </ul>
  </section>

  <section class="card card-back">
    <div class="brand-mark">
      <span class="brand-name">VANTRE</span>
      <span class="brand-sub">THERAPY</span>
    </div>
    <p class="slogan">Mobile Physiotherapy - Your Road To Recovery</p>
    <div class="social">
      <span class="social-dot"></span>
      <span class="social-dot"></span>
    </div>
  </section>
</body>
</html>
```